Medically supervised Weight loss program

I would like to keep a similar layout to the existing business card, maybe adjust the logo a bit. Perhaps new ideas other than the scale. The ZEP which is The parent company should be incorporated into the logo and may be subtle. The logo will also be used on the company website. The colors should represent health and wellness.

Target Market(s)

Overweight age 18 and up

Industry/Entity Type

Medical

Contact Information for Business Card

Same layout preferred

Font styles to use
Other font styles liked:
• Same as attached card

Requirements
Must have
• The circular Logo ZEP needs to be incorporated somehow
Nice to have
• Logo should represent a weight loss program and incorporate the ZEP

```html
<!DOCTYPE html>
<html lang="en">
<head>
<meta charset="utf-8">
<title>ZEP Weight Management – Business Card</title>
<link rel="stylesheet" href="https://fonts.googleapis.com/css2?family=Arimo:wght@700&family=Tinos:ital,wght@0,400;0,700;1,400;1,700&display=swap">
<style>
  :root {
    --backdrop: #5e5e5e;
    --ink: #252525;
    --paper: #ffffff;
    --sky: #14a0c8;
    --teal: #5db7ad;
    --sage: #a9cf92;
    --butter: #f2e47e;
    --divider: #2a2a2a;
    --art-deep: #3f4a44;
    --art-warm: #8a8250;
  }
  * { margin: 0; padding: 0; box-sizing: border-box; }
  html, body { width: 1043px; height: 1200px; overflow: hidden; background: var(--backdrop); }
  .canvas { position: relative; width: 1043px; height: 1200px; }
  .card { position: absolute; left: 118px; width: 818px; height: 468px; }
  .gradient { background: linear-gradient(180deg, var(--sky) 0%, var(--teal) 35%, var(--sage) 65%, var(--butter) 100%); }
  .card-front { top: 96px; }
  .front-title {
    position: absolute; left: 0; right: 0; top: 152px;
    font-family: "Tinos", "Times New Roman", serif; font-weight: 700;
    font-size: 66px; line-height: 78px; text-align: center; color: var(--ink);
  }
  .card-back { top: 636px; background: var(--divider); }
  .back-left { position: absolute; left: 0; top: 0; width: 411px; height: 468px; }
  .back-right { position: absolute; left: 416px; top: 0; width: 402px; height: 468px; background: var(--paper); }
  .brand-name {
    position: absolute; left: 62px; top: 26px; width: 256px; text-align: center;
    font-family: "Tinos", "Times New Roman", serif; font-weight: 700;
    font-size: 32px; line-height: 36px; letter-spacing: 2px; color: var(--ink);
  }
  .illustration {
    position: absolute; left: 62px; top: 76px; width: 256px; height: 160px;
    background: linear-gradient(160deg, var(--art-deep) 0%, var(--art-warm) 100%);
    opacity: 0.55;
  }
  .address {
    position: absolute; left: 44px; top: 264px;
    font-family: "Arimo", Arial, sans-serif; font-weight: 700; font-style: normal;
    font-size: 23px; line-height: 30px; color: var(--ink);
  }
  .phones { margin-top: 12px; }
  .company {
    position: absolute; left: 0; right: 0; top: 54px; text-align: center;
    font-family: "Tinos", "Times New Roman", serif; font-weight: 700;
    font-size: 36px; line-height: 34px; letter-spacing: 2px; color: var(--ink);
  }
  .tagline {
    position: absolute; left: 0; right: 0; top: 128px; text-align: center;
    font-family: "Tinos", "Times New Roman", serif; font-weight: 700; font-style: italic;
    font-size: 25px; color: var(--ink); transform: scaleX(0.86);
  }
  .staff { position: absolute; left: 30px; top: 200px; color: var(--ink); font-family: "Tinos", "Times New Roman", serif; }
  .staff-name { font-weight: 700; font-size: 27px; line-height: 30px; }
  .staff-role { font-style: italic; font-size: 20px; line-height: 25px; }
  .staff-member + .staff-member { margin-top: 14px; }
  .appointment {
    position: absolute; right: 30px; top: 398px;
    font-family: "Tinos", "Times New Roman", serif; font-style: italic;
    font-size: 20px; color: var(--ink);
  }
</style>
</head>
<body>
<main class="canvas">
  <section class="card card-front gradient">
    <h1 class="front-title">ZEP WEIGHT<br>MANAGEMENT</h1>
  </section>

  <section class="card card-back">
    <div class="back-left gradient">
      <div class="brand-name">ZEP</div>
      <div class="illustration" role="img" aria-label="Illustration of a weight scale wrapped by a measuring tape"></div>
      <address class="address">
        <div>1450 MEADOW RIDGE RD.</div>
        <div>SUITE 210</div>
        <div>OAK HOLLOW, NY 11590</div>
        <div class="phones">
          <div>Tel 516-555-0142</div>
          <div>Fax 516-555-0187</div>
        </div>
      </address>
    </div>
    <div class="back-right">
      <h2 class="company">ZEP WEIGHT<br>MANAGEMENT</h2>
      <p class="tagline">Personalized &amp; Medically Supervised</p>
      <div class="staff">
        <div class="staff-member">
          <div class="staff-name">DR. MARTIN FELD</div>
          <div class="staff-role">Diplomate, American Board<br>of Internal Medicine</div>
        </div>
        <div class="staff-member">
          <div class="staff-name">Laura Bennett, NP-BC</div>
          <div class="staff-role">Board Certified Nurse Practitioner</div>
        </div>
      </div>
      <p class="appointment">By Appointment Only</p>
    </div>
  </section>
</main>
</body>
</html>
```